New Business Card (to reflect updated website content and graphics)

I changed some text and graphics on my website, so I need a new business card.

Target Market(s)

Mostly women, ages 30 - 60.

Industry/Entity Type

Life Coaching

Contact Information for Business Card

Included in attached Word document

Font styles to use
Sans Serif

Requirements
Must have
• I am not a creative person, so I will defer to designer. Take a look at my website, and you can get a feel for me, my style, and my target audience. Thank You!

My 3 branding colors are included in attached Word document.

```html
<!DOCTYPE html>
<html lang="en">
<head>
<meta charset="utf-8">
<title>Brightpath Coaching – Business Card</title>
<link href="https://fonts.googleapis.com/css2?family=Montserrat:wght@400;500;700&family=Great+Vibes&display=swap" rel="stylesheet">
<style>
  :root {
    --backdrop: #dcdde2;
    --teal-deep: #2995b0;
    --teal-light: #56c3c4;
    --teal-mist: #cfe9ef;
    --coral: #f37f6e;
    --ink: #1c2a3a;
    --name-teal: #1e8fae;
    --white: #ffffff;
  }
  html, body {
    margin: 0;
    padding: 0;
    width: 1200px;
    height: 1200px;
    overflow: hidden;
    background: var(--backdrop);
  }
  .canvas {
    position: relative;
    width: 1200px;
    height: 1200px;
  }
  .card {
    position: absolute;
    left: 207px;
    width: 785px;
    border-radius: 31px;
    overflow: hidden;
  }
  .card-front {
    top: 99px;
    height: 451px;
    background: var(--teal-deep);
  }
  .word-cloud-area {
    position: absolute;
    left: 168px;
    top: 26px;
    width: 452px;
    height: 404px;
    border-radius: 18px;
    background: radial-gradient(ellipse at center, var(--white) 0%, var(--teal-mist) 100%);
  }
  .card-back {
    top: 642px;
    height: 454px;
    background: var(--white);
  }
  .card-back .waves {
    position: absolute;
    left: 0;
    top: 0;
    width: 785px;
    height: 454px;
  }
  .brand-name {
    position: absolute;
    left: 430px;
    top: 96px;
    width: 360px;
    text-align: center;
    font-family: "Montserrat", sans-serif;
    font-weight: 500;
    font-size: 28px;
    letter-spacing: 1px;
    color: var(--white);
    margin: 0;
  }
  .person-name {
    position: absolute;
    left: 35px;
    top: 160px;
    margin: 0;
    font-family: "Montserrat", sans-serif;
    font-weight: 700;
    font-size: 26px;
    letter-spacing: 0.2px;
    color: var(--name-teal);
  }
  .credentials {
    position: absolute;
    left: 36px;
    top: 207px;
    margin: 0;
    padding: 0;
    list-style: none;
    font-family: "Montserrat", sans-serif;
    font-weight: 400;
    font-size: 19.5px;
    line-height: 28.5px;
    color: var(--ink);
  }
  .contact-list {
    position: absolute;
    left: 36px;
    top: 324px;
    margin: 0;
    padding: 0;
    list-style: none;
    font-family: "Montserrat", sans-serif;
    font-weight: 400;
    font-size: 20px;
    line-height: 32px;
    color: var(--ink);
  }
  .contact-list li {
    display: flex;
    align-items: center;
  }
  .contact-icon {
    width: 20px;
    height: 20px;
    margin-right: 8px;
    flex: none;
  }
  .tagline {
    position: absolute;
    left: 430px;
    top: 334px;
    width: 372px;
    margin: 0;
    text-align: center;
    font-family: "Great Vibes", cursive;
    font-size: 39px;
    line-height: 44px;
    color: var(--coral);
  }
</style>
</head>
<body>
<div class="canvas">

  <section class="card card-front">
    <div class="word-cloud-area" role="img" aria-label="Heart-shaped word cloud of coaching themes such as hope, love, joy, peace and clarity around the line Feel Better, Live Well"></div>
  </section>

  <section class="card card-back">
    <svg class="waves" viewBox="0 0 1264 731" preserveAspectRatio="none" xmlns="http://www.w3.org/2000/svg">
      <path fill="var(--teal-deep)" d="M0 0 H1264 V345 C1000 380 850 300 700 220 C500 110 250 45 0 70 Z"/>
      <path fill="var(--teal-light)" d="M0 85 C250 55 500 110 700 225 C850 310 1000 385 1264 352 V410 C1000 420 850 330 700 240 C500 140 250 110 0 145 Z"/>
      <path fill="var(--coral)" d="M0 130 C260 100 520 160 720 262 C900 352 1050 430 1264 413 V430 C1050 442 900 372 720 282 C520 186 260 168 0 198 Z"/>
    </svg>

    <p class="brand-name">Brightpath Coaching</p>

    <h1 class="person-name">MAREN CASTELL</h1>
    <ul class="credentials">
      <li>Certified Professional Life Coach</li>
      <li>Health &amp; Wellness Coach</li>
      <li>Advanced Grief Renewal Method Specialist</li>
    </ul>

    <ul class="contact-list">
      <li>
        <svg class="contact-icon" viewBox="0 0 24 24" aria-hidden="true">
          <path fill="var(--coral)" d="M6.6 10.8c1.4 2.8 3.8 5.1 6.6 6.6l2.2-2.2c.3-.3.7-.4 1-.2 1.1.4 2.3.6 3.6.6.6 0 1 .4 1 1V20c0 .6-.4 1-1 1C10.6 21 3 13.4 3 4c0-.6.4-1 1-1h3.5c.6 0 1 .4 1 1 0 1.3.2 2.5.6 3.6.1.3 0 .7-.2 1l-2.3 2.2z"/>
        </svg>
        (555) 014-2287
      </li>
      <li>
        <svg class="contact-icon" viewBox="0 0 24 24" aria-hidden="true">
          <rect x="2" y="5" width="20" height="14" rx="1" fill="var(--coral)"/>
          <path d="M3 6 L12 13 L21 6" fill="none" stroke="#ffffff" stroke-width="1.6"/>
        </svg>
        maren@brightpathcoaching.com
      </li>
      <li>
        <svg class="contact-icon" viewBox="0 0 24 24" aria-hidden="true">
          <circle cx="12" cy="12" r="10" fill="var(--coral)"/>
          <path d="M2 12 H22 M12 2 C8 6 8 18 12 22 M12 2 C16 6 16 18 12 22" fill="none" stroke="#ffffff" stroke-width="1.2"/>
        </svg>
        www.brightpathcoaching.com
      </li>
    </ul>

    <p class="tagline">True Happiness<br>Comes From Within</p>
  </section>

</div>
</body>
</html>
```